Mosk trail Website

We need a simple web page design for our businessWe procure and dispose of earthmoving construction equipmentwe also find construction equipment for our customers using our global contacts

Number of Pages Required

1 page

```html
<!DOCTYPE html>
<html lang="en">
<head>
<meta charset="utf-8">
<title>Mosk trail – Earthmoving Construction Equipment</title>
<link href="https://fonts.googleapis.com/css2?family=Montserrat:wght@400;500;600;700&family=Barlow:wght@500;600&family=Barlow+Condensed:wght@500;600&display=swap" rel="stylesheet">
<style>
:root{
  --bg:#e7e7e7;
  --orange:#f6a31c;
  --ink:#231f20;
  --panel:#2b2728;
  --panel-mid:#322e2f;
  --white:#ffffff;
  --muted:#c9c6c4;
  --field:#d6d6d6;
}
*{margin:0;padding:0;box-sizing:border-box}
html,body{width:674px;height:1200px;overflow:hidden;background:var(--bg);font-family:"Montserrat",sans-serif;color:var(--white)}
.page{position:absolute;left:98px;top:6px;width:478px;height:1187px}
.block{position:absolute;left:0;width:478px;overflow:hidden}

/* hero */
.hero{top:0;height:202px;background:linear-gradient(160deg,#3a3c44 0%,#6b5a45 38%,#b8742f 58%,#6a4a2a 80%,#2a2420 100%)}
.hero-photo{position:absolute;inset:0;background:radial-gradient(ellipse at 75% 55%,rgba(214,190,40,.45),rgba(0,0,0,0) 55%),linear-gradient(180deg,rgba(0,0,0,0) 55%,rgba(20,16,12,.55) 100%)}
.topbar{position:absolute;left:0;top:0;width:100%;height:38px;background:rgba(40,38,40,.55);display:flex;align-items:center;padding:0 18px}
.brand{display:flex;flex-direction:column;width:160px}
.brand-name{font-weight:500;font-size:15px;letter-spacing:1px;color:var(--white);line-height:1}
.brand-tag{font-size:5px;color:var(--white);margin-top:2px;padding-left:14px}
.nav{display:flex;gap:12px;margin-left:0;font-family:"Barlow",sans-serif;font-weight:600;font-size:6px;letter-spacing:.2px}
.nav a{color:var(--white);text-decoration:none}
.nav a.active{color:var(--orange)}
.contact-top{margin-left:auto;display:flex;align-items:center;gap:5px}
.contact-top .lines{display:flex;flex-direction:column}
.contact-top .phone{color:var(--orange);font-family:"Barlow",sans-serif;font-weight:600;font-size:8.5px;line-height:1}
.contact-top .mail{font-size:5.5px;margin-top:1px}
.hero-title{position:absolute;left:0;right:0;top:88px;text-align:center;font-weight:700;font-size:17px;line-height:19px}
.btn{display:inline-block;font-family:"Barlow",sans-serif;font-weight:600;font-size:5.5px;letter-spacing:.2px;text-transform:uppercase;text-align:center;line-height:12px;height:13px;color:var(--orange);border:1px solid var(--orange);text-decoration:none}
.btn.solid{background:var(--orange);color:var(--ink)}
.hero .btn{position:absolute;left:201px;top:138px;width:76px;height:15px;line-height:15px;border:none}

/* intro cards */
.cards{top:204px;height:91px;display:flex;gap:2px;background:var(--bg)}
.card{position:relative;flex:1;padding:20px 18px 0}
.card.c1{background:linear-gradient(135deg,#1e2a3c,#3a3a38 50%,#8a6a2c)}
.card.c2{background:linear-gradient(135deg,#2a2e36,#4b4d52 55%,#6b6a50)}
.card.c3{background:linear-gradient(135deg,#2c3040,#4c4450 50%,#9a5a2a)}
.card::before{content:"";position:absolute;inset:0;background:rgba(20,18,20,.45)}
.card p,.card .btn{position:relative}
.card p{font-size:6.5px;line-height:9.5px;width:100px}
.card .btn{position:absolute;left:18px;top:64px;width:52px;height:11px;line-height:9px;font-size:5px}

/* equipment */
.equipment{top:299px;height:294px;display:flex;gap:1px;background:#555}
.equip-intro{width:160px;background:var(--ink);padding:44px 18px 0}
.equip-intro h2{font-weight:600;font-size:13px;line-height:13px}
.equip-intro h3{font-weight:600;font-size:8px;margin-top:1px}
.equip-intro p{font-size:5.5px;line-height:9px;color:var(--muted);margin-top:9px;width:116px}
.equip-intro .btn{margin-top:15px;width:37px;height:11px;line-height:9px;font-size:5px}
.machine{position:relative;flex:1}
.machine.backhoe{background:linear-gradient(180deg,#8aa4bd 0%,#5d7488 30%,#7a7a4a 55%,#3a3a30 80%,#2a2a26 100%)}
.machine.excavator{background:linear-gradient(180deg,#a8b8c0 0%,#8a8570 28%,#c48a2c 50%,#8a5a38 75%,#6a4a34 100%)}
.machine-label{position:absolute;left:0;right:0;top:228px;text-align:center;font-family:"Barlow Condensed",sans-serif;font-weight:500;font-size:11.5px;line-height:13px;text-transform:uppercase;text-shadow:0 1px 2px rgba(0,0,0,.6)}
.arrow{position:absolute;top:238px}

/* values */
.values{top:597px;height:293px;display:flex}
.value{flex:1;display:flex;flex-direction:column;align-items:center;justify-content:center;text-align:center;padding:0 18px;background:var(--panel)}
.value:nth-child(2){background:var(--panel-mid)}
.value h4{font-weight:600;font-size:8.5px;line-height:11px}
.value h4 em{font-style:normal;color:var(--orange)}
.value p{font-size:5.2px;line-height:8.5px;color:var(--muted);margin-top:10px;width:124px}
.value .btn{margin-top:11px;width:52px;height:11px;line-height:9px;font-size:5px}

/* contact */
.hire{top:893px;height:294px;background:linear-gradient(180deg,#3a3a3a 0%,#4a4a48 40%,#2e2e2e 100%)}
.hire-scene{position:absolute;left:0;right:0;bottom:40px;height:120px;background:linear-gradient(180deg,rgba(0,0,0,0),rgba(25,25,25,.6))}
.hire h2{position:absolute;left:0;right:0;top:43px;text-align:center;font-weight:700;font-size:17px}
.hire .lead{position:absolute;left:100px;right:100px;top:64px;text-align:center;font-size:6.5px;line-height:8.5px;color:#ddd}
.form{position:absolute;left:140px;top:95px;width:199px}
.field{position:absolute;height:13px;background:var(--field);color:#555;font-size:5px;line-height:13px;padding-left:8px}
.send{position:absolute;left:200px;top:212px;width:74px;height:14px;line-height:14px;border:none}
.footer{position:absolute;left:28px;right:28px;top:250px;border-top:1px solid #555;padding-top:9px;display:flex;justify-content:space-between;font-size:5px;line-height:10px}
.footer .col{width:140px}
.footer .mid{text-align:center}
.footer .end{text-align:right;padding-right:4px}
.footer .orange{color:var(--orange);font-weight:600}
.footer .strong{font-weight:600}
.social{display:flex;gap:3px;margin-top:1px}
.social span{width:5px;height:5px;background:#bbb}
</style>
</head>
<body>
<div class="page">

  <section class="block hero">
    <div class="hero-photo" role="img" aria-label="Yellow backhoe loader at sunset on an earthmoving site"></div>
    <header class="topbar">
      <div class="brand">
        <span class="brand-name">MOSK TRAIL</span>
        <span class="brand-tag">Earthmoving Construction Equipment</span>
      </div>
      <nav class="nav">
        <a class="active" href="#">COMPANY</a>
        <a href="#">EQUIPMENT</a>
        <a href="#">INDUSTRY</a>
        <a href="#">SERVICES</a>
        <a href="#">CONTACT</a>
      </nav>
      <div class="contact-top">
        <svg width="16" height="16" viewBox="0 0 16 16" aria-hidden="true">
          <circle cx="8" cy="8" r="8" fill="#f6a31c"/>
          <path d="M5.2 4.4l1.4-.3.8 2-1 .7a5 5 0 0 0 2.6 2.6l.7-1 2 .8-.3 1.4c-3.6.3-6.5-2.6-6.2-6.2z" fill="#231f20"/>
        </svg>
        <div class="lines">
          <span class="phone">0400 128 764</span>
          <span class="mail">hello@mosktrail.example</span>
        </div>
      </div>
    </header>
    <h1 class="hero-title">For all your<br>earth moving needs</h1>
    <a class="btn solid" href="#">Get a free quote</a>
  </section>

  <section class="block cards">
    <div class="card c1" role="img" aria-label="Excavator moving soil at dusk">
      <p>We supply new, used and reconditioned earthmoving equipment</p>
      <a class="btn" href="#">Equipment</a>
    </div>
    <div class="card c2" role="img" aria-label="Site workers in hard hats and hi-vis vests">
      <p>We deliver professional earthmoving equipment hire services</p>
      <a class="btn" href="#">Services</a>
    </div>
    <div class="card c3" role="img" aria-label="Harbour bridge at sunset">
      <p>Looking for earthmoving jobs or more information from Mosk trail</p>
      <a class="btn" href="#">Contact us</a>
    </div>
  </section>

  <section class="block equipment">
    <div class="equip-intro">
      <h2>Earthmoving</h2>
      <h3>Equipment</h3>
      <p>We offers a diverse range of mining, construction and forestry machinery, designed to cater to the professional needs of every customer.</p>
      <a class="btn" href="#">More</a>
    </div>
    <div class="machine backhoe" role="img" aria-label="Yellow 4x4 backhoe loader on a dirt mound">
      <div class="machine-label">4x4 Backhoe<br>Loader</div>
      <svg class="arrow" style="right:3px" width="10" height="10" viewBox="0 0 10 10" aria-hidden="true"><circle cx="5" cy="5" r="4.5" fill="none" stroke="#f6a31c" stroke-width=".8"/><path d="M4 3l2 2-2 2" fill="none" stroke="#f6a31c" stroke-width=".8"/></svg>
    </div>
    <div class="machine excavator" role="img" aria-label="Yellow tracked excavator on red earth">
      <div class="machine-label">Tracked<br>Excavators</div>
      <svg class="arrow" style="left:3px" width="10" height="10" viewBox="0 0 10 10" aria-hidden="true"><circle cx="5" cy="5" r="4.5" fill="none" stroke="#f6a31c" stroke-width=".8"/><path d="M6 3L4 5l2 2" fill="none" stroke="#f6a31c" stroke-width=".8"/></svg>
    </div>
  </section>

  <section class="block values">
    <div class="value">
      <h4>With <em>over 30 years</em><br>of experience,</h4>
      <p>Mosk trail has established itself as a pioneer supplier of new, used and reconditioned earthmoving equipment.</p>
      <a class="btn" href="#">About us</a>
    </div>
    <div class="value">
      <h4>Our <em>dedicated<br>team</em></h4>
      <p>is always on-hand to assist you and advise on the most suitable equipment for your earthmoving project.</p>
      <a class="btn solid" href="#">Consult now</a>
    </div>
    <div class="value">
      <h4>Our <em>goal</em> is to<br>provide</h4>
      <p>high-quality products and ensure your machine runs effectively. Get in touch today!</p>
      <a class="btn" href="#">Contact us</a>
    </div>
  </section>

  <section class="block hire">
    <div class="hire-scene" role="img" aria-label="Monochrome earthmoving site with loaders and excavators"></div>
    <h2>Hire Mosk trail Today!</h2>
    <p class="lead">If you would like a FREE quote or have any questions about our services please fill below form and send us message</p>
    <div class="form">
      <div class="field" style="left:0;top:0;width:96px">Enter your Name</div>
      <div class="field" style="left:103px;top:0;width:96px">Email</div>
      <div class="field" style="left:0;top:21px;width:96px">Phone</div>
      <div class="field" style="left:103px;top:21px;width:96px">Subject</div>
      <div class="field" style="left:0;top:42px;width:199px;height:66px;line-height:11px">Message ...</div>
    </div>
    <a class="btn solid send" href="#">Send your message</a>
    <footer class="footer">
      <div class="col">
        <div>(c) 2018 Mosk trail. All rights reserved.</div>
        <div class="social"><span></span><span></span><span></span><span></span><span></span></div>
      </div>
      <div class="col mid">
        <div>e. hello@mosktrail.example</div>
        <div class="orange">P. 0400 128 764</div>
      </div>
      <div class="col end">
        <div>14 Ridgeway Rd, Kelby, TAS 7010</div>
        <div class="strong">CONTACT US</div>
      </div>
    </footer>
  </section>

</div>
</body>
</html>
```